Window and GutterCleaning Flyer A5 size double sided.

We need a double sided A5 flyer. Side 1, is for window cleaning, side 2 is for gutter cleaning. Licensed by Borough of Halvern Council.
Phone number 0800 315 4720.
Business address 7 Tarnlow Brae, North Pellin Edinburgh EH14 3RW.
www.clearpane-vista-services.com
We use a LoftPro Gutter inspection Cam to view your gutters first to see if they need doing.
Window cleaning ; Professional window cleaning services, what we offer, water fed pole window cleaning able to reach windows up to 60 feet.
Conservatory cleaning.
Conservatory roof cleaning.
Fascias & Soffits cleaning.
Excellent Customer Service.
Target Market(s)
domestic houses
Industry/Entity Type
window cleaning
Look and feel
Each slider illustrates characteristics of the customer's brand and the style your logo design should communicate.

```html
<!DOCTYPE html>
<html lang="en">
<head>
<meta charset="utf-8">
<title>ClearPane Vista – Window &amp; Gutter Flyers</title>
<link href="https://fonts.googleapis.com/css2?family=Nunito:wght@400;600;700;800;900&display=swap" rel="stylesheet">
<style>
:root{
  --page:#eef0f3;
  --paper:#eaf3fb;
  --blue:#2a7fc9;
  --blue-deep:#1c5fb0;
  --navy:#123f8f;
  --ink:#0f2f6b;
  --sky:#cfe3f5;
  --green:#3f7a2c;
  --tick:#4caf50;
  --white:#ffffff;
}
*{box-sizing:border-box;margin:0;padding:0}
html,body{width:683px;height:1200px;overflow:hidden}
body{background:var(--page);font-family:"Nunito",Arial,sans-serif;position:relative}
.flyer{position:absolute;left:134px;width:414px;height:586px;background:var(--paper);overflow:hidden;box-shadow:0 3px 10px rgba(0,0,0,.18)}
.flyer--window{top:6px}
.flyer--gutter{top:606px}
.abs{position:absolute}

/* header */
.brand{left:14px;top:30px;display:flex;align-items:center;gap:6px}
.brand__mark{width:12px;height:12px;background:var(--blue)}
.brand__name{font-weight:800;font-size:13px;color:var(--navy);line-height:1}
.header-band{left:128px;top:0;width:286px;height:86px;background:linear-gradient(90deg,var(--blue-deep),var(--blue));clip-path:polygon(13% 0,100% 0,100% 100%,0 100%);color:var(--white);padding:20px 0 0 44px}
.header-band__title{font-weight:800;font-size:17px;line-height:1.08;text-transform:uppercase}
.header-band__sub{font-size:9.5px;margin-top:3px;opacity:.95}

.photo{display:block}

/* window side */
.headline{left:228px;top:118px;color:var(--navy);font-weight:900;line-height:1}
.headline__big{font-size:34px;display:block}
.headline__mid{font-size:22px;display:block;font-weight:800}
.intro{left:192px;top:236px;width:222px;height:96px;background:linear-gradient(90deg,#8fc0ea,#c4def4);clip-path:polygon(4% 0,100% 0,100% 100%,0 100%);padding:10px 10px 0 18px;font-size:7.1px;line-height:1.28;color:var(--ink)}
.method{left:12px;top:366px;width:392px;font-size:8.2px;font-weight:700;color:var(--navy);text-align:center;line-height:1.3}
.benefits{left:0;top:396px;width:234px;height:110px;background:linear-gradient(90deg,var(--blue-deep),var(--blue));clip-path:polygon(0 0,90% 0,100% 100%,0 100%);color:var(--white);padding:8px 0 0 14px}
.benefits__title{font-size:17px;font-weight:800;line-height:1}
.benefits__sub{font-size:9px;margin-bottom:5px}
.ticks{list-style:none}
.ticks li{display:flex;align-items:center;gap:5px;font-size:6.8px;line-height:1.2;margin-bottom:4px}
.ticks svg{flex:none}
.tagline{left:14px;top:518px;color:var(--navy);line-height:1.05}
.tagline__big{font-size:19px;font-weight:900;display:block}
.tagline__small{font-size:13px;font-weight:700;display:block}

/* footer */
.footer{left:0;bottom:0;width:262px;height:14px;background:var(--blue);color:var(--white);font-size:5.6px;display:flex;justify-content:space-around;align-items:center}
.phone{right:0;bottom:0;width:170px;height:38px;background:var(--sky);clip-path:polygon(9% 0,100% 0,100% 100%,0 100%);display:flex;align-items:center;justify-content:center;gap:6px;color:var(--navy);font-weight:800;font-size:16px;padding-left:12px}

/* gutter side */
.cam-panel{left:0;top:116px;width:414px;height:174px;background:linear-gradient(90deg,#1a5fb1,#3a8fd6)}
.cam-copy{left:14px;top:126px;color:var(--white);width:220px}
.cam-copy__lead{font-size:8px}
.cam-copy__title{font-size:19px;font-weight:800;line-height:1.08;text-transform:uppercase;margin-bottom:6px}
.cam-copy .ticks li{font-size:8px;margin-bottom:5px}
.label{height:18px;padding:0 16px 0 10px;background:var(--green);color:var(--white);font-size:10px;font-weight:700;display:flex;align-items:center;clip-path:polygon(0 0,85% 0,100% 50%,85% 100%,0 100%)}
.offer{left:14px;top:442px;width:216px;height:116px;background:var(--white);border:2px solid var(--blue);padding:8px 0 0 12px;line-height:1}
.offer__a{font-size:26px;font-weight:900;color:var(--blue);display:block}
.offer__b{font-size:13.5px;font-weight:800;color:var(--navy);display:block;margin:3px 0 2px}
.offer__c{font-size:40px;font-weight:900;color:var(--blue);display:block}
.offer-tail{left:228px;top:438px}
</style>
</head>
<body>

<!-- Side 1: window cleaning -->
<section class="flyer flyer--window">
  <div class="abs brand"><span class="brand__mark"></span><span class="brand__name">ClearPane Vista</span></div>
  <div class="abs header-band">
    <div class="header-band__title">Professional Window<br>Cleaning Services</div>
    <div class="header-band__sub">Serving Domestic Homes Across Edinburgh</div>
  </div>

  <svg class="abs photo" style="left:0;top:102px" width="222" height="242" role="img" aria-label="Photo of a window cleaner in blue overalls cleaning a large glass window with a squeegee">
    <defs><linearGradient id="gWorker" x1="0" y1="0" x2="1" y2="1"><stop offset="0" stop-color="#dfe7ee"/><stop offset=".55" stop-color="#9fb8d2"/><stop offset="1" stop-color="#5d85b5"/></linearGradient></defs>
    <rect width="222" height="242" fill="url(#gWorker)"/>
  </svg>

  <h1 class="abs headline"><span class="headline__big">Reliable,</span><span class="headline__mid">Friendly &amp; Fully</span><span class="headline__mid">Insured.</span></h1>

  <p class="abs intro">Regular window cleaning helps to avoid the build-up of dirt and residue on the glass, meaning more light can get into your home or premises and can also improve its external appearance. We clean outside windows on houses and commercial buildings. In addition, we offer a conservatory cleaning service, gutter/fascia cleaning and painting, and builders cleans for those who have had work completed on their property.</p>

  <p class="abs method">Our industry has developed a safer method of cleaning windows through the use of long reaching telescopic poles (water fed poles), allowing windows to be cleaned from the safety of the ground.</p>

  <div class="abs benefits">
    <div class="benefits__title">Benefits</div>
    <div class="benefits__sub">of pure hot water system</div>
    <ul class="ticks">
      <li><svg width="8" height="8" viewBox="0 0 10 10"><circle cx="5" cy="5" r="5" fill="var(--tick)"/><path d="M2.6 5.2l1.6 1.6 3.2-3.4" stroke="#fff" stroke-width="1.4" fill="none"/></svg>Frames and sills are cleaned at the same time</li>
      <li><svg width="8" height="8" viewBox="0 0 10 10"><circle cx="5" cy="5" r="5" fill="var(--tick)"/><path d="M2.6 5.2l1.6 1.6 3.2-3.4" stroke="#fff" stroke-width="1.4" fill="none"/></svg>Reduced disturbance to you and your garden</li>
      <li><svg width="8" height="8" viewBox="0 0 10 10"><circle cx="5" cy="5" r="5" fill="var(--tick)"/><path d="M2.6 5.2l1.6 1.6 3.2-3.4" stroke="#fff" stroke-width="1.4" fill="none"/></svg>Increased privacy</li>
      <li><svg width="8" height="8" viewBox="0 0 10 10"><circle cx="5" cy="5" r="5" fill="var(--tick)"/><path d="M2.6 5.2l1.6 1.6 3.2-3.4" stroke="#fff" stroke-width="1.4" fill="none"/></svg>Improved access</li>
    </ul>
  </div>

  <svg class="abs photo" style="left:200px;top:398px" width="214" height="130" role="img" aria-label="Photos of a brick house front and a water fed pole brush cleaning a window">
    <defs><linearGradient id="gHouse" x1="0" y1="0" x2="1" y2="0"><stop offset="0" stop-color="#8a6a5a"/><stop offset=".5" stop-color="#b99b86"/><stop offset="1" stop-color="#d6e1ea"/></linearGradient></defs>
    <polygon points="30,0 214,0 214,130 0,130" fill="url(#gHouse)"/>
    <line x1="120" y1="0" x2="104" y2="130" stroke="var(--paper)" stroke-width="3"/>
  </svg>

  <div class="abs tagline"><span class="tagline__big">No need to move</span><span class="tagline__small">your car out the driveway!</span></div>

  <div class="abs footer"><span>www.clearpane-vista-services.com</span><span>info@clearpane-vista-services.com</span></div>
  <div class="abs phone">
    <svg width="16" height="16" viewBox="0 0 20 20"><circle cx="10" cy="10" r="9" fill="none" stroke="var(--blue)" stroke-width="1.8"/><path d="M7 5.5l1.6 2.4-1 1.1c.6 1.3 1.5 2.2 2.8 2.8l1.1-1 2.4 1.6-.8 1.7c-3.4-.2-6.7-3.5-6.9-6.9z" fill="var(--blue)"/></svg>
    0800 315 4720
  </div>
</section>

<!-- Side 2: gutter cleaning -->
<section class="flyer flyer--gutter">
  <div class="abs brand"><span class="brand__mark"></span><span class="brand__name">ClearPane Vista</span></div>
  <div class="abs header-band">
    <div class="header-band__title">Gutter Cleaning &amp;<br>Inspection Services</div>
    <div class="header-band__sub">Prevent Water Damage – Clean Gutters Keep Homes Safe!</div>
  </div>

  <div class="abs cam-panel"></div>
  <svg class="abs photo" style="left:232px;top:116px" width="182" height="174" role="img" aria-label="Photo of a gutter inspection camera monitor on a pole">
    <defs><linearGradient id="gCam" x1="0" y1="0" x2="1" y2="1"><stop offset="0" stop-color="#3a4048"/><stop offset=".6" stop-color="#6a93c4"/><stop offset="1" stop-color="#9fc7ea"/></linearGradient></defs>
    <polygon points="34,0 182,0 182,174 0,174" fill="url(#gCam)"/>
  </svg>
  <div class="abs cam-copy">
    <div class="cam-copy__lead">We use</div>
    <div class="cam-copy__title">LoftPro Gutter<br>Inspection Cam</div>
    <ul class="ticks">
      <li><svg width="8" height="8" viewBox="0 0 10 10"><circle cx="5" cy="5" r="5" fill="var(--tick)"/><path d="M2.6 5.2l1.6 1.6 3.2-3.4" stroke="#fff" stroke-width="1.4" fill="none"/></svg>We inspect your gutters before cleaning</li>
      <li><svg width="8" height="8" viewBox="0 0 10 10"><circle cx="5" cy="5" r="5" fill="var(--tick)"/><path d="M2.6 5.2l1.6 1.6 3.2-3.4" stroke="#fff" stroke-width="1.4" fill="none"/></svg>Efficient &amp; safe from the ground – no ladders needed</li>
      <li><svg width="8" height="8" viewBox="0 0 10 10"><circle cx="5" cy="5" r="5" fill="var(--tick)"/><path d="M2.6 5.2l1.6 1.6 3.2-3.4" stroke="#fff" stroke-width="1.4" fill="none"/></svg>Removes leaves, moss, and all debris</li>
      <li><svg width="8" height="8" viewBox="0 0 10 10"><circle cx="5" cy="5" r="5" fill="var(--tick)"/><path d="M2.6 5.2l1.6 1.6 3.2-3.4" stroke="#fff" stroke-width="1.4" fill="none"/></svg>Ideal for hard-to-reach areas and high buildings</li>
    </ul>
  </div>

  <svg class="abs photo" style="left:0;top:296px" width="244" height="142" role="img" aria-label="Photo of a gutter vacuum nozzle over a garden lawn">
    <defs><linearGradient id="gVac" x1="0" y1="0" x2="1" y2="1"><stop offset="0" stop-color="#5a6a7a"/><stop offset=".5" stop-color="#7f9c6a"/><stop offset="1" stop-color="#a8c48d"/></linearGradient></defs>
    <polygon points="0,0 244,0 214,142 0,142" fill="url(#gVac)"/>
  </svg>
  <svg class="abs photo" style="left:212px;top:296px" width="202" height="100" role="img" aria-label="Photo of a roof edge showing gutter, fascia and soffit">
    <defs><linearGradient id="gRoof" x1="0" y1="0" x2="1" y2="1"><stop offset="0" stop-color="#f4f6f8"/><stop offset="1" stop-color="#8d6b58"/></linearGradient></defs>
    <polygon points="30,0 202,0 202,100 0,100" fill="url(#gRoof)"/>
  </svg>
  <svg class="abs photo" style="left:226px;top:396px" width="188" height="154" role="img" aria-label="Photo of a smiling customer service agent wearing a headset">
    <defs><linearGradient id="gAgent" x1="0" y1="0" x2="1" y2="1"><stop offset="0" stop-color="#e8e2da"/><stop offset="1" stop-color="#c9b7a3"/></linearGradient></defs>
    <rect width="188" height="154" fill="url(#gAgent)"/>
  </svg>

  <div class="abs label" style="left:262px;top:318px">Gutter</div>
  <div class="abs label" style="left:234px;top:354px">Fascia</div>
  <div class="abs label" style="left:216px;top:392px">Soffit</div>

  <svg class="abs offer-tail" width="34" height="30" viewBox="0 0 34 30"><polygon points="0,4 34,0 0,28" fill="var(--white)" stroke="var(--blue)" stroke-width="2"/><rect x="0" y="6" width="3" height="20" fill="var(--white)"/></svg>
  <div class="abs offer">
    <span class="offer__a">Book a free</span>
    <span class="offer__b">GUTTER INSPECTION</span>
    <span class="offer__c">TODAY!</span>
  </div>

  <div class="abs footer"><span>www.clearpane-vista-services.com</span><span>info@clearpane-vista-services.com</span></div>
  <div class="abs phone">
    <svg width="16" height="16" viewBox="0 0 20 20"><circle cx="10" cy="10" r="9" fill="none" stroke="var(--blue)" stroke-width="1.8"/><path d="M7 5.5l1.6 2.4-1 1.1c.6 1.3 1.5 2.2 2.8 2.8l1.1-1 2.4 1.6-.8 1.7c-3.4-.2-6.7-3.5-6.9-6.9z" fill="var(--blue)"/></svg>
    0800 315 4720
  </div>
</section>

</body>
</html>
```